College Admissions Consulting needs a small street facing sign for new office location.

I need a graphic design to be used inside window for a banner/sign in office location on a high walking traffic city street, for my company, Campus Lantern. I work with high school students and families on the college planning and selection application process. Please check out the website to learn more about what I do (www.mycampuslantern.example). The banner will be used to market our services at our office location. The final design should utilize logo colors, phone number, and website/email information. I'd like to incorporate a my picture in someway because of face recognition. To be printed on a posterboard or vinyl banner.

Target Market(s)

Parents of high school aged children.

Industry/Entity Type

Education

Font styles to use
Sans Serif

Colors
abd037

Requirements
Must have
• Clean, attractive, and professional design. Attract the attention of people walking by. Information must be clear and readable (phone/email, etc.).
Nice to have
• Utilize the picture with crossed arms (without the brown background on picture).
Emphasize tagline:
Mastering The College Admission Process
....with personalized, professional guidance in planning, selecting, and applying to the right colleges.

```html
<!DOCTYPE html>
<html lang="en">
<head>
<meta charset="UTF-8">
<title>Campus Lantern – Mastering the College Admission Process</title>
<link rel="stylesheet" href="https://fonts.googleapis.com/css2?family=Montserrat:wght@600;800&family=Lora:ital,wght@1,400&display=swap">
<style>
  :root {
    --lime: #abd037;
    --butter: #fbda6b;
    --ink: #141414;
    --paper: #ffffff;
    --portrait-dark: #1c1c1c;
    --portrait-mid: #5a4a42;
  }
  * { margin: 0; padding: 0; box-sizing: border-box; }
  html, body {
    width: 1200px;
    height: 800px;
    overflow: hidden;
    background: var(--lime);
  }
  .sign {
    position: relative;
    width: 1200px;
    height: 800px;
    overflow: hidden;
    background: var(--lime);
  }
  .sign__backdrop {
    position: absolute;
    inset: 0;
    width: 1200px;
    height: 800px;
  }
  .paper-corner, .paper-band { fill: var(--butter); }
  .tagline {
    position: absolute;
    left: 92px;
    top: 214px;
    width: 820px;
  }
  .tagline__headline {
    font-family: "Montserrat", sans-serif;
    font-weight: 800;
    font-size: 64px;
    line-height: 78px;
    text-transform: uppercase;
    white-space: nowrap;
    color: var(--ink);
  }
  .tagline__support {
    margin-top: 6px;
    font-family: "Lora", serif;
    font-style: italic;
    font-size: 28.5px;
    line-height: 35px;
    white-space: nowrap;
    color: var(--paper);
  }
  .brand {
    position: absolute;
    left: 92px;
    top: 610px;
    font-family: "Montserrat", sans-serif;
    font-weight: 800;
    font-size: 30px;
    line-height: 36px;
    text-transform: uppercase;
    color: var(--ink);
  }
  .contact {
    position: absolute;
    left: 92px;
    top: 748px;
    display: flex;
    gap: 30px;
    font-family: "Montserrat", sans-serif;
    font-weight: 600;
    font-size: 17px;
    line-height: 22px;
    white-space: nowrap;
    color: var(--ink);
    list-style: none;
  }
</style>
</head>
<body>
  <main class="sign">
    <svg class="sign__backdrop" viewBox="0 0 1200 800" xmlns="http://www.w3.org/2000/svg">
      <defs>
        <linearGradient id="portrait-tone" x1="0" y1="0" x2="0" y2="1">
          <stop offset="0" stop-color="#5a4a42"/>
          <stop offset="0.45" stop-color="#1c1c1c"/>
          <stop offset="1" stop-color="#1c1c1c"/>
        </linearGradient>
      </defs>
      <path class="paper-corner" d="M948 0 C960 40 990 70 1030 110 C1080 160 1110 200 1140 240 C1160 262 1180 270 1200 272 L1200 0 Z"/>
      <path class="portrait" role="img" aria-label="Portrait of the consultant, smiling with arms crossed, wearing a black top"
            fill="url(#portrait-tone)"
            d="M880 72 C840 80 828 130 836 180 C842 230 860 280 880 310 C850 330 800 360 780 420 C765 470 748 530 744 580 C742 620 760 660 800 700 L810 720 L1080 720 L1088 560 C1092 470 1080 400 1060 370 C1040 340 1020 320 1010 300 C1030 270 1050 220 1060 180 C1068 130 1040 84 980 74 C950 68 910 66 880 72 Z"/>
      <path class="paper-band" d="M0 712 C60 705 140 708 220 702 C300 698 360 712 420 716 C500 722 560 728 640 736 C720 744 760 740 800 706 C860 690 920 690 980 684 C1060 676 1120 676 1200 662 L1200 800 L0 800 Z"/>
    </svg>

    <section class="tagline">
      <h1 class="tagline__headline">Mastering the<br>College Admission<br>Process!</h1>
      <p class="tagline__support">with personalized, professional guidance in planning,<br>selecting, and applying to the right colleges.</p>
    </section>

    <p class="brand">Campus Lantern</p>

    <ul class="contact">
      <li class="contact__phone">(555) 014-2270</li>
      <li class="contact__web">www.mycampuslantern.example</li>
      <li class="contact__email">hello@mycampuslantern.example</li>
    </ul>
  </main>
</body>
</html>
```